Proposal Poster, posters for kids to hold

I am proposing to my girlfriend soon, I need two posters made for my kids to hold one I want to say “be my mommy”
And the other “will you marry my daddy”
Both in horizontal format. I plan on sending the files to a print shop to get them printed on a large poster. Simple is fine with maybe a few graphics. Open to anything. Kids will be holding it from the beach as we are on a jet ski close to shore. Must be readable font from a short distance

• Cute but readable font from a distance

```html
<!DOCTYPE html>
<html lang="en">
<head>
<meta charset="utf-8">
<title>Will You Marry My Daddy – Proposal Poster</title>
<link rel="stylesheet" href="https://fonts.googleapis.com/css2?family=Dancing+Script:wght@700&family=Lobster&display=swap">
<style>
  :root {
    --page-bg: #e8e8e8;
    --poster-pink-light: #fbdde3;
    --poster-pink: #f6c2cc;
    --poster-pink-deep: #f2aebb;
    --slate-blue: #525c85;
    --love-red: #f0294a;
    --heart-red: #c8193a;
    --scene-lilac: #e9d6e6;
    --scene-navy: #4a4f86;
  }
  * { margin: 0; padding: 0; box-sizing: border-box; }
  html, body {
    width: 798px;
    height: 1200px;
    overflow: hidden;
    background: var(--page-bg);
  }
  .canvas {
    position: relative;
    width: 798px;
    height: 1200px;
  }
  .poster {
    position: absolute;
    left: 49px;
    top: 338px;
    width: 700px;
    height: 524px;
    overflow: hidden;
    background:
      radial-gradient(ellipse at 50% 35%, var(--poster-pink-light) 0%, transparent 60%),
      radial-gradient(ellipse at 15% 85%, var(--poster-pink-deep) 0%, transparent 55%),
      linear-gradient(160deg, var(--poster-pink) 0%, var(--poster-pink-light) 50%, var(--poster-pink) 100%);
    box-shadow: 0 3px 6px rgba(0, 0, 0, 0.35);
  }
  .headline {
    position: absolute;
    left: 0;
    width: 100%;
    line-height: 1;
    white-space: nowrap;
    text-align: center;
  }
  .headline--will-you {
    font-family: "Dancing Script", cursive;
    font-weight: 700;
    color: var(--slate-blue);
    font-size: 112px;
    top: 10px;
    left: -2px;
  }
  .headline--marry {
    font-family: "Lobster", cursive;
    color: var(--love-red);
    font-size: 150px;
    top: 95px;
    left: -20px;
    letter-spacing: -2px;
  }
  .headline--my {
    font-family: "Dancing Script", cursive;
    font-weight: 700;
    color: var(--slate-blue);
    font-size: 112px;
    top: 222px;
    left: -42px;
  }
  .headline--daddy {
    font-family: "Lobster", cursive;
    color: var(--love-red);
    font-size: 150px;
    top: 300px;
    left: -82px;
    letter-spacing: -2px;
  }
  .heart {
    position: absolute;
    fill: none;
    stroke: var(--heart-red);
    stroke-width: 4;
    stroke-linejoin: round;
  }
  .heart--left { left: 72px; top: 62px; width: 54px; height: 46px; transform: rotate(-12deg); }
  .heart--right { left: 596px; top: 100px; width: 64px; height: 54px; transform: rotate(10deg); }
  .ring-icon {
    position: absolute;
    left: 460px;
    top: 44px;
    width: 24px;
    height: 20px;
    border-radius: 4px;
    background: var(--slate-blue);
    opacity: 0.7;
  }
  .wedding-scene {
    position: absolute;
    left: 510px;
    top: 287px;
    width: 190px;
    height: 237px;
    border-radius: 95px 95px 0 0;
    background: linear-gradient(180deg, var(--scene-lilac) 0%, #f4e8f0 45%, var(--scene-navy) 160%);
  }
</style>
</head>
<body>
  <main class="canvas">
    <section class="poster" aria-label="Will You Marry My Daddy proposal poster">
      <svg class="heart heart--left" viewBox="0 0 54 46" aria-hidden="true">
        <path d="M27 42 C10 30 3 20 6 11 C9 3 20 2 27 13 C32 3 44 2 48 10 C51 19 42 30 27 42 Z"/>
      </svg>
      <svg class="heart heart--right" viewBox="0 0 54 46" aria-hidden="true">
        <path d="M27 42 C10 30 3 20 6 11 C9 3 20 2 27 13 C32 3 44 2 48 10 C51 19 42 30 27 42 Z"/>
      </svg>

      <div class="wedding-scene" role="img" aria-label="Illustration of a bride and groom standing under a flowered wedding arch"></div>

      <h1 class="headline headline--will-you">Will You</h1>
      <div class="ring-icon" role="img" aria-label="Small engagement ring icon"></div>
      <p class="headline headline--marry">marry</p>
      <p class="headline headline--my">my</p>
      <p class="headline headline--daddy">Daddy</p>
    </section>
  </main>
</body>
</html>
```